Professional DJ Business Card

Business card for giving out to clubs and venues or interested groups that are in need of a professional DJ. I want something artistic and catchy/alluring, with a minimalist approach that gets just the vital amount of info and leaves the rest for inquiry via contacting me. Ideally I would like one side to have an image of something cool like an eye and my name, then the other side be the contact info, I am definitely feeling a black or dark colored card, but I am open to other designs. I am uploading a picture that I made that reflects a little of what I am *kind of* looking for.

Industry/Entity Type

Business

Contact Information for Business Card

Tomas Halvik (Voxtel)
Professional DJ (West Coast)
EDM (Deep/House/Techno), Hip Hop, Latin, Trap.
Cell: 555-274-9163
Email: Voxtelofficial@mailnest.net
www.beatcloudia.net/yourtuneisfading

```html
<!DOCTYPE html>
<html lang="en">
<head>
<meta charset="utf-8">
<title>Voxtel – Professional DJ Business Card</title>
<link rel="stylesheet" href="https://fonts.googleapis.com/css2?family=Open+Sans:wght@400;600;700&display=swap">
<style>
  :root {
    --backdrop: #2b2623;
    --card: #141414;
    --card-edge: #1f1f1f;
    --ink: #ffffff;
    --ink-soft: #e6e6e6;
  }
  * { margin: 0; padding: 0; box-sizing: border-box; }
  html, body {
    width: 1200px; height: 844px; overflow: hidden;
    background: var(--backdrop);
    font-family: "Open Sans", Arial, sans-serif;
    color: var(--ink);
  }
  .stage {
    position: relative; width: 1200px; height: 844px;
    display: flex; align-items: center; justify-content: center; gap: 60px;
  }
  .card {
    position: relative; width: 525px; height: 300px;
    background: var(--card);
    border: 1px solid var(--card-edge);
    box-shadow: 0 18px 40px rgba(0,0,0,.45);
  }
  .brand {
    position: absolute; display: flex; align-items: center; gap: 12px;
    font-weight: 400; color: var(--ink); letter-spacing: 1px;
  }
  .brand-dot { border-radius: 50%; background: var(--ink); flex: none; }
  .card-front .brand { top: 62px; right: 40px; font-size: 48px; }
  .card-front .brand-dot { width: 18px; height: 18px; }
  .holder { position: absolute; left: 34px; bottom: 52px; }
  .holder-name { font-weight: 700; font-size: 17px; }
  .holder-role { font-size: 14px; color: var(--ink-soft); }
  .contact {
    position: absolute; right: 30px; bottom: 54px;
    list-style: none; text-align: right; font-size: 13.5px; line-height: 22px;
  }
  .contact li { display: flex; justify-content: flex-end; align-items: center; gap: 8px; }
  .contact svg { width: 11px; height: 11px; flex: none; }
  .card-back .brand {
    top: 88px; left: 0; right: 0; justify-content: center; font-size: 52px;
  }
  .card-back .brand-dot { width: 20px; height: 20px; }
  .genres {
    position: absolute; left: 0; right: 0; top: 196px;
    text-align: center; font-weight: 600; font-size: 13px;
  }
</style>
</head>
<body>
<main class="stage">
  <section class="card card-front">
    <div class="brand"><span class="brand-dot"></span>Voxtel</div>
    <div class="holder">
      <p class="holder-name">Tomas Halvik</p>
      <p class="holder-role">Professional DJ</p>
    </div>
    <ul class="contact">
      <li>555-274-9163
        <svg viewBox="0 0 12 12" aria-hidden="true"><path d="M2.5 1l2 2-1 1.2a7 7 0 0 0 4.3 4.3L9 7.5l2 2-1.3 1.5C5.5 11 1 6.5 1 2.3z" fill="#fff"/></svg>
      </li>
      <li>Voxtelofficial@mailnest.net
        <svg viewBox="0 0 12 12" aria-hidden="true"><rect x="1" y="2.5" width="10" height="7" fill="#fff"/><path d="M1 2.5l5 4 5-4" stroke="#141414" fill="none"/></svg>
      </li>
      <li>www.beatcloudia.net/yourtuneisfading
        <svg viewBox="0 0 12 12" aria-hidden="true"><path d="M5 7l2-2M4.5 5.5l-2 2a1.7 1.7 0 0 0 2.4 2.4l2-2M7.5 6.5l2-2a1.7 1.7 0 0 0-2.4-2.4l-2 2" stroke="#fff" stroke-width="1.2" fill="none" stroke-linecap="round"/></svg>
      </li>
    </ul>
  </section>
  <section class="card card-back">
    <div class="brand"><span class="brand-dot"></span>Voxtel</div>
    <p class="genres">EDM (Deep/House/Techno), Hip Hop, Latin, Trap.</p>
  </section>
</main>
</body>
</html>
```